KRT World Class Organisation Poster

We are looking for ideas on how to design this poster to best capture the message we are trying to convey (KRT World Class Organisation). Make sure that these 5 statements feature on the poster.

Logo has been provided, please include in your poster design.

Please use the logo design as the inspiration for your poster layout, drawing on the DNA double helix symbol.

Also refer to the layout of the attached poster. We would like to retain the layout however it should be visually appealing - use your imagination & creativity!
Updates

Target Market(s)

internal company use only - logo provided which will need to be included.

Requirements
Must have
• The poster should be in portrait format as it will be printed in 'A3' size.

Must include the KRT logo provided - see attached file.
Nice to have
• Please use the logo design as the inspiration for your poster layout, drawing on the DNA double helix symbol.

```html
<!DOCTYPE html>
<html lang="en">
<head>
<meta charset="utf-8">
<title>KRT World Class Organisation Poster</title>
<link href="https://fonts.googleapis.com/css2?family=Hind:wght@300;400;700&display=swap" rel="stylesheet">
<style>
  :root {
    --page: #ffffff;
    --sky-top: #2c78b8;
    --sky-mid: #4596cf;
    --sky-low: #8fcdee;
    --sky-base: #b7def3;
    --glow: rgba(220, 244, 255, 0.55);
    --trace: rgba(190, 228, 250, 0.18);
    --cream: #f4f1c9;
    --lime: #b8d432;
    --frame-blue-light: #39b4e6;
    --frame-blue-dark: #0d78b8;
    --panel-blue: #d3eaf6;
    --frame-green-light: #cfe04a;
    --frame-green-dark: #99b521;
    --panel-green: #f2f5dd;
    --ink: #1e1e1e;
  }
  * { margin: 0; padding: 0; box-sizing: border-box; }
  html, body { width: 1200px; height: 900px; overflow: hidden; background: var(--page); }
  body { position: relative; font-family: "Hind", Arial, sans-serif; }

  .poster {
    position: absolute; left: 317px; top: 50px; width: 566px; height: 800px;
    background: linear-gradient(180deg, var(--sky-top) 0%, var(--sky-mid) 42%, var(--sky-low) 72%, var(--sky-base) 100%);
    overflow: hidden;
  }
  .circuit-backdrop {
    position: absolute; inset: 0;
    background:
      radial-gradient(ellipse 70% 30% at 50% 62%, var(--glow), rgba(255,255,255,0) 70%),
      radial-gradient(ellipse 45% 25% at 90% 12%, var(--trace), rgba(255,255,255,0) 70%),
      radial-gradient(ellipse 50% 30% at 20% 90%, var(--trace), rgba(255,255,255,0) 70%),
      linear-gradient(180deg, rgba(0,40,90,0.12) 0%, rgba(0,40,90,0) 35%);
  }

  .headline { position: absolute; left: 0; top: 0; width: 100%; font-weight: 700; }
  .headline span { position: absolute; line-height: 1; white-space: nowrap; text-shadow: 1px 2px 3px rgba(0,30,70,0.35); }
  .headline-lead { left: 47px; top: 40px; font-size: 42px; color: var(--cream); }
  .headline-main { left: 110px; top: 76px; font-size: 64px; color: var(--lime); letter-spacing: -0.5px; }
  .headline-tail { right: 44px; top: 128px; font-size: 45px; color: var(--cream); }

  .value-card { position: absolute; }
  .value-frame {
    position: absolute; inset: 0; border-radius: 14px;
    background: linear-gradient(135deg, var(--frame-blue-light), var(--frame-blue-dark));
    box-shadow: 0 3px 6px rgba(0,40,80,0.25);
  }
  .value-card.is-green .value-frame { background: linear-gradient(135deg, var(--frame-green-light), var(--frame-green-dark)); }
  .value-panel {
    position: absolute; top: 8px; right: 8px; bottom: 12px; left: 37px;
    background: var(--panel-blue); border-radius: 10px;
  }
  .value-tab {
    position: absolute; top: 8px; left: 8px; width: 40px; height: 50px;
    background: var(--panel-blue); border-radius: 10px 0 0 18px;
  }
  .value-card.is-green .value-panel,
  .value-card.is-green .value-tab { background: var(--panel-green); }
  .value-number {
    position: absolute; left: 14px; top: 14px; font-size: 42px; font-weight: 700; color: var(--ink); line-height: 1;
  }
  .value-text {
    position: absolute; font-size: 12px; font-weight: 300; line-height: 14.6px; color: var(--ink); white-space: nowrap;
  }
  .value-text strong { font-weight: 700; }

  .point-down::after, .point-up::before {
    content: ""; position: absolute; left: 50%; transform: translateX(-50%);
    border-left: 70px solid transparent; border-right: 70px solid transparent;
  }
  .point-down::after { bottom: -14px; border-top: 14px solid var(--frame-blue-dark); }
  .point-up::before { top: -14px; border-bottom: 14px solid var(--frame-blue-light); }

  .card-1 { left: 48px; top: 253px; width: 223px; height: 144px; }
  .card-2 { left: 295px; top: 212px; width: 224px; height: 174px; }
  .card-3 { left: 48px; top: 418px; width: 471px; height: 112px; }
  .card-4 { left: 48px; top: 556px; width: 223px; height: 186px; }
  .card-5 { left: 295px; top: 556px; width: 224px; height: 144px; }

  .card-1 .value-text { left: 56px; top: 33px; }
  .card-2 .value-text { left: 57px; top: 31px; }
  .card-3 .value-text { left: 56px; top: 32px; }
  .card-4 .value-text { left: 56px; top: 33px; }
  .card-5 .value-text { left: 57px; top: 33px; }
</style>
</head>
<body>
  <main class="poster">
    <div class="circuit-backdrop" role="img" aria-label="Faint blue circuit-board texture with glowing network nodes"></div>

    <h1 class="headline">
      <span class="headline-lead">KRT is a</span>
      <span class="headline-main">World Class</span>
      <span class="headline-tail">organisation</span>
    </h1>

    <section class="value-card card-1 point-down">
      <div class="value-frame"></div><div class="value-panel"></div><div class="value-tab"></div>
      <span class="value-number">1</span>
      <p class="value-text">We employ <strong>World Class</strong><br><strong>Business Systems</strong> to<br>exceed expectations by<br>driving innovation at the<br>forefront of technology.</p>
    </section>

    <section class="value-card card-2 point-down">
      <div class="value-frame"></div><div class="value-panel"></div><div class="value-tab"></div>
      <span class="value-number">2</span>
      <p class="value-text">We manufacture using<br>innovative <strong>World Class</strong><br><strong>Manufacturing Processes</strong><br>and lean technologies<br>adapted to produce<br>safe, effective &amp; reliable<br>products to meet our<br>patients’ needs.</p>
    </section>

    <section class="value-card card-3 is-green">
      <div class="value-frame"></div><div class="value-panel"></div><div class="value-tab"></div>
      <span class="value-number">3</span>
      <p class="value-text">We strive to be <strong>World Class Colleagues</strong> who are professional, motivated,<br>helpful and positive. We are accountable in achieving our goals. We are<br>innovative, always challenge the status-quo and open to new ideas.</p>
    </section>

    <section class="value-card card-4 point-up">
      <div class="value-frame"></div><div class="value-panel"></div><div class="value-tab"></div>
      <span class="value-number">4</span>
      <p class="value-text">We work with <strong>World Class</strong><br><strong>Service Providers</strong> who<br>are leaders and innovators<br>that challenge the status-<br>quo and focus on quality<br>excellence and continuous<br>improvement to exceed<br>customer expectations.</p>
    </section>

    <section class="value-card card-5 point-up">
      <div class="value-frame"></div><div class="value-panel"></div><div class="value-tab"></div>
      <span class="value-number">5</span>
      <p class="value-text">We believe <strong>World Class</strong><br><strong>Customer Service</strong> is<br>to deliver the ultimate<br>customer satisfaction<br>every time.</p>
    </section>
  </main>
</body>
</html>
```